Professional Website for Corvell Laundry Company

Corvell Laundry Company is a family-owned laundry service provider that has been serving Midtown Atlanta for over 45 years. We provide express clothing and linen washing services to residential and commercial clients in Atlanta and surrounding areas.

The final website and logo design should convey professionalism and give the customer a sense of security in having their personal items laundered with us.

Target Market(s)

Commercial Businesses and high net worth personal customers

Industry/Entity Type

Professional Laundry Services

Coding

Coded - Design and coding required

Number of Pages Required

5+ page

Font styles to use
Sans Serif

Colors
0054AA
0677BA
7BADD7
CADEEF
E8F1F8

Requirements
Must have
• I would like to have the following elements on my website: 1. Blog page 2. Contact Us Form 3. Sign up for service (sample attached) 4. Sections outlined in the content copy page 5. Links to social media accounts.
Nice to have
• A great example is https://www.quorvadip.example/laundry-pick-up-and-delivery/?utm_term=pick%20up%20and%20delivery%20laundry%20service&utm_campaign=*QV%20United%20States%20%7C%20Search%20(Broad%20KWs)&utm_source=bing&utm_medium=ppc&hsa_acc=1203948576&hsa_cam=50219384761&hsa_grp=9081726354637281&hsa_ad=&hsa_src=o&hsa_tgt=kwd-27391046582917:loc-190&hsa_kw=pick%20up%20and%20delivery%20laundry%20service&hsa_mt=e&hsa_net=bing&hsa_ver=3&msclkid=3a9f0c1b2d4e5f60718293a4b5c6d7e8

```html
<!DOCTYPE html>
<html lang="en">
<head>
<meta charset="utf-8">
<title>Corvell Laundry Company</title>
<link href="https://fonts.googleapis.com/css2?family=Montserrat:wght@500;600&family=Roboto:wght@400;500;700;900&family=Great+Vibes&display=swap" rel="stylesheet">
<style>
:root{
  --navy:#0054AA;
  --blue:#0677BA;
  --sky:#7BADD7;
  --pale:#CADEEF;
  --mist:#E8F1F8;
  --teal:#3BA3C7;
  --ink:#2b2b2b;
  --grey:#555;
  --white:#fff;
}
*{margin:0;padding:0;box-sizing:border-box}
html,body{width:1200px;height:3783px;overflow:hidden}
body{position:relative;font-family:'Roboto',sans-serif;color:var(--ink);background:var(--white)}
.abs{position:absolute}
a{color:inherit;text-decoration:none}

/* top bar */
.topbar{left:0;top:0;width:1200px;height:26px;background:var(--sky);color:var(--white);font-size:9px;letter-spacing:.2px}
.topbar span{position:absolute;top:8px;display:flex;align-items:center;gap:4px}
.signup-tab{left:952px;top:0;width:86px;height:56px;background:var(--pale);color:var(--blue);font-size:10px;font-weight:700;text-align:center;padding-top:12px;clip-path:polygon(0 0,100% 0,100% 100%,50% 80%,0 100%)}

/* header */
.logo{font-family:'Montserrat',sans-serif;font-weight:500;color:#111;line-height:1}
.logo .l1{font-size:31px;display:block}
.logo .l2{font-size:23px;display:block;margin-top:2px;padding-left:73px}
.nav{top:62px;left:623px;display:flex;gap:0;font-size:12px;font-weight:500}
.nav a{position:absolute;white-space:nowrap}
.nav .active{color:var(--blue)}

/* hero */
.hero{left:0;top:97px;width:1200px;height:501px;background:radial-gradient(ellipse at 60% 85%,#c9742b 0%,#5a3a2a 30%,transparent 55%),linear-gradient(180deg,#1e2a44 0%,#2e3550 45%,#3a2f33 75%,#1a1a22 100%)}
.hero-pre{left:160px;top:235px;color:var(--white);font-size:23px;font-weight:400;letter-spacing:.5px}
.hero-title{left:160px;top:266px;color:var(--white);font-size:39px;font-weight:700;line-height:41px;letter-spacing:.5px}
.hero-rule{left:123px;top:334px;width:34px;height:3px;background:var(--white)}
.btn-call{left:160px;top:391px;width:190px;height:35px;background:var(--blue);color:var(--white);font-size:13px;font-weight:500;display:flex;align-items:center;justify-content:center;gap:7px;border-radius:2px}

/* section headings */
.eyebrow{width:1200px;left:0;text-align:center;color:var(--blue);font-size:12px;font-weight:500;letter-spacing:.3px}
.sec-title{width:1200px;left:0;text-align:center;font-size:28px;font-weight:700;color:#222}

/* how we work */
.step{width:260px;text-align:center}
.step-icon{width:114px;height:114px;border-radius:50%;background:var(--sky);margin:0 auto;display:flex;align-items:center;justify-content:center}
.step h3{font-size:15px;font-weight:500;margin-top:22px;color:#222}
.step p{font-size:11px;line-height:15.5px;color:var(--grey);margin-top:14px;padding:0 8px}

/* about */
.about-photo{left:0;top:1034px;width:580px;height:373px;background:linear-gradient(90deg,#e8ecee 0%,#cfd6da 40%,#d8b8a0 70%,#ece7e2 100%)}
.badge{left:76px;top:1148px;width:130px;height:130px;border-radius:50%;background:var(--white);text-align:center;box-shadow:0 0 0 6px rgba(255,255,255,.5);padding-top:24px}
.badge b{display:block;font-size:44px;color:var(--blue);line-height:44px;font-weight:700}
.badge span{font-size:12px;line-height:15px;color:#333;display:block}
.script{font-family:'Great Vibes',cursive;color:var(--blue);font-size:62px;line-height:1}
.about-title{font-size:29px;font-weight:700;color:#222}
.body-text{font-size:11px;line-height:15.5px;color:var(--grey)}
.btn{background:var(--blue);color:var(--white);font-size:11px;font-weight:500;display:flex;align-items:center;justify-content:center;border-radius:2px}

/* stats */
.stats{left:0;top:1464px;width:1200px;height:121px;background:linear-gradient(90deg,var(--sky),#8db8dc 50%,var(--sky))}
.stat{width:200px;text-align:center;color:var(--white);top:30px}
.stat b{display:block;font-size:38px;font-weight:900;line-height:40px}
.stat span{font-size:13px}

/* services */
.svc-intro{left:230px;top:1692px;width:740px;text-align:center;font-size:11px;line-height:15.5px;color:var(--grey)}
.card{top:1768px;width:275px;height:378px;color:var(--white);text-align:center}
.card .photo{height:209px;width:100%}
.card .icon{position:absolute;left:105px;top:177px;width:64px;height:64px;border-radius:50%;display:flex;align-items:center;justify-content:center}
.card h3{font-size:17px;font-weight:700;margin-top:34px}
.card p{font-size:10.5px;line-height:13.5px;padding:4px 14px 0}
.card .more{position:absolute;left:0;width:100%;top:340px;font-size:11px;font-weight:700}

/* why */
.why-photo{left:612px;top:2203px;width:588px;height:358px;background:linear-gradient(135deg,#2b3342 0%,#3a4660 35%,#1f2636 60%,#6b5a48 85%,#8a7a66 100%)}
.why-sub{left:160px;top:2366px;font-size:14px;font-weight:500;color:#222}
.btn-outline{border:2px solid var(--blue);color:var(--blue);font-size:11px;font-weight:500;display:flex;align-items:center;justify-content:center;border-radius:2px}

/* testimonials */
.quote{width:270px}
.quote .mark{color:var(--sky);font-size:40px;font-weight:900;line-height:30px;font-family:Georgia,serif}
.quote p{font-size:12px;line-height:17px;color:#333;margin-top:4px}
.author{display:flex;align-items:center;gap:10px;margin-top:22px}
.avatar{width:54px;height:54px;border-radius:50%;background:linear-gradient(135deg,#c8ccd2,#8d9097)}
.author b{font-family:'Montserrat',sans-serif;font-size:15px;font-weight:600;color:#222;display:block}
.author span{font-size:10.5px;color:#444}
.dots{left:580px;top:2928px;display:flex;gap:6px}
.dots i{width:6px;height:6px;border-radius:50%;background:var(--pale);display:block}
.dots i:first-child{background:var(--sky)}

/* form */
.form-band{left:0;top:2999px;width:1200px;height:417px;background:linear-gradient(90deg,#7aacd6,#86b4db 50%,#7aacd6)}
.form-title{left:0;width:1200px;top:3053px;text-align:center;color:var(--white);font-size:32px;font-weight:900;letter-spacing:-.5px}
.lbl{font-size:10.5px;color:var(--white)}
.field{width:265px;height:39px;background:var(--white);border:1px solid #dde6ef}
.select{display:flex;align-items:center;justify-content:space-between;padding:0 14px;font-size:10px;color:#777}
.btn-next{left:610px;top:3319px;width:262px;height:38px;background:var(--blue);border:2px solid var(--white);color:var(--white);font-size:15px;font-weight:700;display:flex;align-items:center;justify-content:center}

/* footer */
.foot-h{font-size:13px;font-weight:700;color:#222;top:3543px}
.foot-list{font-size:11px;line-height:21px;color:#333}
.foot-list .active{color:var(--blue);font-weight:500}
.contact-row{display:flex;gap:8px;font-size:10px;color:#333;line-height:16px;margin-bottom:4px}
.social{width:24px;height:24px;border-radius:50%;border:1px solid #555;top:3588px}
.bottombar{left:0;top:3730px;width:1200px;height:53px;background:var(--teal);color:var(--white);font-size:10px;text-align:center;line-height:53px}
</style>
</head>
<body>

<!-- Top bar -->
<div class="abs topbar">
  <span style="left:160px"><svg width="8" height="10" viewBox="0 0 8 10"><path d="M4 0a3 3 0 0 0-3 3c0 2.3 3 7 3 7s3-4.7 3-7a3 3 0 0 0-3-3zm0 4.2A1.2 1.2 0 1 1 4 1.8a1.2 1.2 0 0 1 0 2.4z" fill="#fff"/></svg>210 N. HARLOW AVENUE SUITE 4B, MIDVALE, GA 30301</span>
  <span style="left:495px"><svg width="10" height="8" viewBox="0 0 10 8"><rect x="0" y="0" width="10" height="8" rx="1" fill="#fff"/><path d="M0 0l5 4 5-4" stroke="#7BADD7" fill="none"/></svg>SALES@CORVELLLAUNDRY.EXAMPLE</span>
  <span style="left:758px"><svg width="9" height="9" viewBox="0 0 10 10"><path d="M2 0l2 2-1 2c1 1.5 2 2.5 3 3l2-1 2 2-2 2C4 9 1 6 0 2z" fill="#fff"/></svg>404-555-0183</span>
</div>
<div class="abs signup-tab">SIGN UP NOW</div>

<!-- Header -->
<div class="abs logo" style="left:160px;top:30px">
  <span class="l1">Corvell Laundry</span>
  <span class="l2">Company</span>
</div>
<nav class="abs nav">
  <a class="active" style="left:0">HOME</a>
  <a style="left:75px">ABOUT US</a>
  <a style="left:173px">SERVICES</a>
  <a style="left:267px">BLOG</a>
  <a style="left:340px">CONTACT US</a>
</nav>

<!-- Hero -->
<div class="abs hero" role="img" aria-label="City skyline at night with light trails on a highway"></div>
<div class="abs hero-pre">WANT TO GET YOUR</div>
<h1 class="abs hero-title">CLOTHES<br>CLEANED? QUICKLY</h1>
<div class="abs hero-rule"></div>
<a class="abs btn-call"><svg width="14" height="14" viewBox="0 0 10 10"><path d="M2 0l2 2-1 2c1 1.5 2 2.5 3 3l2-1 2 2-2 2C4 9 1 6 0 2z" fill="#fff"/></svg>CALL US 404-555-0183</a>

<!-- How we work -->
<div class="abs eyebrow" style="top:655px">CORVELL LAUNDRY COMPANY ALWAYS</div>
<h2 class="abs sec-title" style="top:670px">THIS IS HOW WE WORK</h2>

<div class="abs step" style="left:168px;top:733px">
  <div class="step-icon"><svg width="56" height="56" viewBox="0 0 56 56" fill="none" stroke="#fff" stroke-width="3" stroke-linecap="round"><rect x="10" y="6" width="30" height="42" rx="5"/><path d="M17 17h16M17 25h16M17 33h8"/><path d="M46 22L30 40l-2 7 7-3 16-17z"/></svg></div>
  <h3>Sign Up</h3>
  <p>Give us a call at <b style="color:#333">404-555-0183</b> or use our sign up page to schedule service. You can control the frequency of how often we process your laundry.</p>
</div>
<div class="abs step" style="left:469px;top:733px">
  <div class="step-icon"><svg width="60" height="56" viewBox="0 0 60 56" fill="#fff"><circle cx="26" cy="16" r="11"/><path d="M6 46c0-11 9-17 20-17 5 0 9 1 12 3-5 3-8 8-8 14z"/><circle cx="45" cy="43" r="10"/><path d="M40 43l4 4 6-7" stroke="#7BADD7" stroke-width="3" fill="none"/></svg></div>
  <h3>Fill Out a Customer Profile</h3>
  <p>When setting up your customer profile you can detail how you want your laundry processed; hangers for shirts, pants folded, etc. You can select your laundry detergents, bleaches and softeners from a list of provided products.</p>
</div>
<div class="abs step" style="left:770px;top:733px">
  <div class="step-icon"><svg width="58" height="56" viewBox="0 0 58 56" fill="none" stroke="#fff" stroke-width="3" stroke-linejoin="round"><path d="M8 16l18-8 18 8v10"/><path d="M8 16v24l18 8"/><path d="M8 16l18 8 18-8M26 24v10"/><circle cx="42" cy="40" r="11"/><path d="M42 34v6l4 3"/></svg></div>
  <h3>Schedule a Pickup</h3>
  <p>Place your clothes in the Corvell Laundry Company bag and leave it out on your scheduled pickup day. We will process your clothing as instructed and deliver it back to your doorstep within 24 hours.</p>
</div>

<!-- About -->
<div class="abs about-photo" role="img" aria-label="Woman smelling freshly washed towel by a bright window"></div>
<div class="abs badge"><b>45</b><span>Years of<br>Experience</span></div>
<div class="abs script" style="left:610px;top:1040px">About</div>
<h2 class="abs about-title" style="left:613px;top:1122px">CORVELL LAUNDRY COMPANY</h2>
<p class="abs body-text" style="left:614px;top:1167px;width:430px">Corvell Laundry Company is a family-owned laundry service provider that has been serving Midtown Atlanta for over 45 years. We are proud to offer high quality and convenient services to the area residents and business owners and strive to keep our customers' clothing in tip top shape.</p>
<p class="abs body-text" style="left:614px;top:1246px;width:430px">Whether you have commercial laundry needs, are washing clothes for your family, or want to relax that weekend and have us pick up and wash/dry/fold for you, the professionals at Corvell Laundry Company are ready to meet your goals. We provide express clothes and linen washing services to residential and commercial clients in Atlanta and surrounding areas.</p>
<a class="abs btn" style="left:614px;top:1345px;width:125px;height:35px">LEARN MORE</a>

<!-- Stats -->
<div class="abs stats">
  <div class="abs stat" style="left:161px"><b>350+</b><span>Employees</span></div>
  <div class="abs stat" style="left:386px"><b>15</b><span>Branches</span></div>
  <div class="abs stat" style="left:612px"><b>1600+</b><span>Jobs Done</span></div>
  <div class="abs stat" style="left:838px"><b>4554+</b><span>People Like Us</span></div>
</div>

<!-- Services -->
<h2 class="abs sec-title" style="top:1643px;font-size:31px">OUR SERVICES</h2>
<p class="abs svc-intro">Running a small business is not easy and the last thing you need is another tedious action item like doing laundry on your to-do list. Whether it is towels, linens or uniforms, outsourcing your launder needs to Corvell Laundry Company will allow you to focus on your business. We promise to provide on-time and reliability, period.</p>

<div class="abs card" style="left:34px;background:var(--sky)">
  <div class="photo" role="img" aria-label="Staff member sorting garments on a rack" style="background:linear-gradient(135deg,#6e6f73,#c9c6c0 50%,#8a8478)"></div>
  <div class="icon" style="background:var(--sky)"><svg width="30" height="30" viewBox="0 0 30 30" fill="none" stroke="#fff" stroke-width="2.5"><circle cx="15" cy="10" r="6"/><path d="M3 22c4-2 7 2 12 2s8-4 12-2M3 27h24"/></svg></div>
  <h3>Commercial Services</h3>
  <p>Our state-of-the-art laundry processing center is designed for the efficiency our commercial clients expect. Our trained staff handles routine processing and the difficult issues of commercial laundry to deliver consistent quality and value.</p>
  <div class="more">LEARN MORE ›</div>
</div>
<div class="abs card" style="left:320px;background:var(--blue)">
  <div class="photo" role="img" aria-label="White delivery van parked outdoors" style="background:linear-gradient(160deg,#b7c6cf,#e9eef0 45%,#7e8d7a)"></div>
  <div class="icon" style="background:var(--blue)"><svg width="34" height="24" viewBox="0 0 34 24" fill="none" stroke="#fff" stroke-width="2.2"><path d="M2 4h18v14H2zM20 9h7l5 5v4H20"/><circle cx="8" cy="20" r="3" fill="#0677BA"/><circle cx="26" cy="20" r="3" fill="#0677BA"/></svg></div>
  <h3>Pickup and Delivery</h3>
  <p>Pickup and delivery available in the Atlanta, Midtown and Buckhead area. No delivery charge in the delivery area. We do charge extra for same day or Sunday service.</p>
  <div class="more">LEARN MORE ›</div>
</div>
<div class="abs card" style="left:606px;background:var(--navy)">
  <div class="photo" role="img" aria-label="Row of suit jackets on hangers" style="background:linear-gradient(135deg,#222a3a,#3b4763 50%,#6f6a63)"></div>
  <div class="icon" style="background:var(--navy)"><svg width="30" height="30" viewBox="0 0 30 30" fill="none" stroke="#fff" stroke-width="2.5" stroke-linecap="round"><path d="M12 8a3 3 0 1 1 3 3v4L3 22h24L15 15"/><path d="M7 22v5h16v-5"/></svg></div>
  <h3>Dry Cleaning</h3>
  <p>Do you have garments or linens that are made of delicate fabrics that should not be machine washed? We offer professional dry cleaning services for our customers and businesses.</p>
  <div class="more">LEARN MORE ›</div>
</div>
<div class="abs card" style="left:893px;background:var(--teal)">
  <div class="photo" role="img" aria-label="Worker loading linens into an industrial washer" style="background:linear-gradient(135deg,#8d8f95,#c9c4c0 45%,#9b3a3a 75%,#6a6d72)"></div>
  <div class="icon" style="background:var(--teal)"><svg width="26" height="30" viewBox="0 0 26 30" fill="none" stroke="#fff" stroke-width="2.5"><rect x="2" y="2" width="22" height="26" rx="3"/><circle cx="13" cy="17" r="6"/><path d="M2 8h22"/></svg></div>
  <h3>Professional Laundry Services</h3>
  <p>If you want to enjoy the perks of dry cleaning without all the chemicals, we offer a wash, dry, and press/iron service. You can relax knowing that your clothes will be flawlessly cleaned.</p>
  <div class="more">LEARN MORE ›</div>
</div>

<!-- Why choose -->
<div class="abs script" style="left:158px;top:2212px;font-size:58px">Why Choose</div>
<h2 class="abs about-title" style="left:160px;top:2288px">CORVELL LAUNDRY COMPANY</h2>
<div class="abs why-sub">We Help You Optimize Your Time</div>
<p class="abs body-text" style="left:160px;top:2395px;width:425px">Laundry is time consuming, especially for multi-tasking entrepreneurs. Corvell Laundry Company makes a simple promise, we will give you your time back to focus on your business. Our goal is to provide your business with a clean, dry, and properly folded product every single time.</p>
<a class="abs btn" style="left:160px;top:2503px;width:128px;height:36px">VIEW DETAILS</a>
<a class="abs btn-outline" style="left:293px;top:2503px;width:182px;height:36px">CLICK HERE TO FILL OUT FORM</a>
<div class="abs why-photo" role="img" aria-label="Close view of tailored jackets hanging in a row"></div>

<!-- Testimonials -->
<div class="abs eyebrow" style="top:2616px">WHAT OUR CLIENT SAYS</div>
<h2 class="abs sec-title" style="top:2632px;font-size:31px">TESTIMONIALS</h2>

<div class="abs quote" style="left:166px;top:2706px">
  <div class="mark">“</div>
  <p>Lorem ipsum dolor sit amet, consectetur adipiscing elit. Etiam ultrices nunc sit amet lacus imperdiet bibendum. Aliquam ac ligula a massa semper congue</p>
  <div class="author"><div class="avatar" role="img" aria-label="Customer portrait"></div><div><b>Delano Marsh</b><span>Verified Customer</span></div></div>
</div>
<div class="abs quote" style="left:467px;top:2706px">
  <div class="mark">“</div>
  <p>Lorem ipsum dolor sit amet, consectetur adipiscing elit. Etiam ultrices nunc sit amet lacus imperdiet bibendum. Aliquam ac ligula a massa semper congue</p>
  <div class="author"><div class="avatar" role="img" aria-label="Customer portrait" style="background:linear-gradient(135deg,#8a6a55,#3e2e26)"></div><div><b>Delano Marsh</b><span>Verified Customer</span></div></div>
</div>
<div class="abs quote" style="left:761px;top:2706px">
  <div class="mark">“</div>
  <p>Lorem ipsum dolor sit amet, consectetur adipiscing elit. Etiam ultrices nunc sit amet lacus imperdiet bibendum. Aliquam ac ligula a massa semper congue</p>
  <div class="author"><div class="avatar" role="img" aria-label="Customer portrait" style="background:linear-gradient(135deg,#d5dbe0,#9aa3ab)"></div><div><b>Delano Marsh</b><span>Verified Customer</span></div></div>
</div>
<div class="abs dots"><i></i><i></i><i></i><i></i></div>

<!-- Form -->
<div class="abs form-band" role="img" aria-label="Soft blue tinted background of folded linens"></div>
<h2 class="abs form-title">LETS GET STARTED</h2>

<div class="abs lbl" style="left:336px;top:3102px">First Name</div>
<div class="abs lbl" style="left:608px;top:3102px">Last Name</div>
<div class="abs field" style="left:336px;top:3118px"></div>
<div class="abs field" style="left:608px;top:3118px"></div>

<div class="abs lbl" style="left:336px;top:3168px">Email</div>
<div class="abs lbl" style="left:608px;top:3168px">Phone</div>
<div class="abs field" style="left:336px;top:3184px"></div>
<div class="abs field" style="left:608px;top:3184px"></div>

<div class="abs lbl" style="left:336px;top:3234px">Best Time to Reach You?</div>
<div class="abs lbl" style="left:608px;top:3234px">How Can We Help ?</div>
<div class="abs field select" style="left:336px;top:3250px">Morning (7am-12pm)<svg width="9" height="5"><path d="M0 0h9L4.5 5z" fill="#333"/></svg></div>
<div class="abs field select" style="left:608px;top:3250px">Need to Schedule Pick up<svg width="9" height="5"><path d="M0 0h9L4.5 5z" fill="#333"/></svg></div>

<div class="abs lbl" style="left:336px;top:3301px">What is Your Zip Code</div>
<div class="abs field" style="left:336px;top:3319px"></div>
<a class="abs btn-next">NEXT<svg class="abs" style="right:14px;top:8px" width="20" height="20" viewBox="0 0 20 20" fill="none" stroke="#fff" stroke-width="1.5"><circle cx="10" cy="10" r="9"/><path d="M8 6l4 4-4 4"/></svg></a>

<!-- Footer -->
<div class="abs logo" style="left:483px;top:3460px">
  <span class="l1">Corvell Laundry</span>
  <span class="l2">Company</span>
</div>

<div class="abs foot-h" style="left:160px">MAILING US</div>
<div class="abs" style="left:160px;top:3579px;width:248px;height:43px;border:1px solid #bbb;font-size:9px;color:#777;padding:16px 13px;letter-spacing:.5px">ENTER YOUR EMAIL ID</div>
<a class="abs btn-outline" style="left:160px;top:3629px;width:126px;height:38px">SUBSCRIBE</a>

<div class="abs foot-h" style="left:470px">QUICK LINKS</div>
<div class="abs foot-list" style="left:470px;top:3575px">
  <div class="active">HOME</div><div>ABOUT US</div><div>SERVICES</div><div>BLOG</div><div>CONTACT US</div>
</div>

<div class="abs foot-h" style="left:660px">CONTACT DETAILS</div>
<div class="abs" style="left:663px;top:3574px">
  <div class="contact-row"><svg width="10" height="10" viewBox="0 0 10 10"><path d="M2 0l2 2-1 2c1 1.5 2 2.5 3 3l2-1 2 2-2 2C4 9 1 6 0 2z" fill="#0677BA"/></svg>404-555-0183</div>
  <div class="contact-row" style="margin-top:6px"><svg width="10" height="10" viewBox="0 0 10 8"><rect x=".5" y=".5" width="9" height="7" fill="none" stroke="#0677BA"/><path d="M.5.5l4.5 4 4.5-4" stroke="#0677BA" fill="none"/></svg>SALES@CORVELLLAUNDRY.EXAMPLE</div>
  <div class="contact-row" style="margin-top:6px"><svg width="10" height="10" viewBox="0 0 10 10"><circle cx="5" cy="5" r="4" fill="none" stroke="#0677BA"/><path d="M5 2.5V5l2 1" stroke="#0677BA" fill="none"/></svg><span>MONDAY - FRIDAY : 7AM TO 5PM<br>SUNDAY: CLOSED</span></div>
</div>

<div class="abs foot-h" style="left:916px">JOIN US</div>
<div class="abs social" style="left:918px"></div>
<div class="abs social" style="left:949px"></div>
<div class="abs social" style="left:981px"></div>
<div class="abs social" style="left:1012px"></div>

<div class="abs bottombar">CORVELL LAUNDRY COMPANY . © 2022 ALL RIGHTS RESERVED.</div>

</body>
</html>
```